Web Design Project

I am looking for a simple website to promote my business called Wyllard Benick Consulting. We provide consulting and implementation services for finance and supply chain processes and systems.

We want to project a professional but innovative image. I have attached a copy of our logo. It is not necessary to stick with the colours in the logo - we encourage you to experiment with the colours and even to change the colours of the logo to fit with your design. Although, on the front page we would like to have the logo with its original colours.

Required sections:
About
What we do
Clients
Contact
Updates

Target Market(s)

Medium to large companies including multi-nationals in all industries.

Industry/Entity Type

Finance

Requirements
Must have
• Required sections:
About
What we do
Clients
Contact

```html
<!DOCTYPE html>
<html lang="en">
<head>
<meta charset="utf-8">
<title>Wyllard Benick Consulting</title>
<link rel="stylesheet" href="https://fonts.googleapis.com/css2?family=Open+Sans:wght@400;600;700;800&display=swap">
<style>
:root{
  --green:#8cc63e;
  --green-dark:#74a82e;
  --ink:#333333;
  --muted:#777777;
  --line:#e2e2e2;
  --soft:#f3f3f3;
  --tile:#2a2a2a;
  --footer:#2b2b2b;
  --footer-deep:#1f1f1f;
  --footer-text:#a9a9a9;
  --white:#ffffff;
}
*{margin:0;padding:0;box-sizing:border-box}
html,body{width:829px;height:1200px;overflow:hidden}
body{font-family:"Open Sans",Arial,sans-serif;color:var(--ink);background:var(--white);font-size:7px;line-height:1.5;position:relative}
.wrap{width:700px;margin:0 auto;position:relative}
a{color:inherit;text-decoration:none}
.green{color:var(--green)}

/* header */
.site-header{height:48px;border-bottom:1px solid var(--line)}
.site-header .wrap{display:flex;align-items:center;justify-content:space-between;height:48px}
.brand{display:flex;align-items:center;gap:6px;font-weight:700;font-size:9px;color:var(--green-dark)}
.brand-dot{width:18px;height:18px;border-radius:50%;background:var(--green)}
.main-nav{display:flex;gap:14px;font-size:7px;color:var(--muted)}
.main-nav .active{color:var(--green);font-weight:600}

/* hero */
.hero{height:214px;background:linear-gradient(#fafafa,#eeeeee);position:relative}
.hero .wrap{display:flex;height:214px}
.hero-photo{width:420px;height:214px;background:linear-gradient(120deg,#cfd3d6,#e9e4dd 55%,#b9c0c6)}
.hero-copy{padding:40px 0 0 22px;width:280px}
.hero-copy h1{font-size:24px;font-weight:800;line-height:1.1;color:#222}
.hero-copy h2{font-size:13px;font-weight:400;color:var(--green);margin:4px 0 8px}
.hero-copy p{color:var(--muted);font-size:6.5px}
.btn{display:inline-block;background:var(--green);color:var(--white);font-weight:600;font-size:6.5px;padding:4px 12px;border-radius:2px}
.hero-copy .btn{margin-top:10px}
.slide-arrow{position:absolute;top:92px;width:16px;height:26px;background:#3a3a3a;display:flex;align-items:center;justify-content:center}
.slide-arrow.prev{left:0}.slide-arrow.next{right:0}
.dots{display:flex;justify-content:center;gap:4px;height:16px;align-items:center}
.dots i{width:5px;height:5px;border-radius:50%;background:#cfcfcf}
.dots i.on{background:var(--green)}

/* features */
.features .wrap{display:flex;justify-content:space-between;padding-top:8px;height:124px}
.feature{width:210px;text-align:center}
.feature svg{display:block;margin:0 auto 6px}
.feature h3{font-size:7.5px;font-weight:700;margin-bottom:4px}
.feature p{color:var(--muted);font-size:6px}
.more{color:var(--green);font-size:6px;font-weight:600;display:inline-block;margin-top:4px}

/* clients */
.section-title{text-align:center;font-size:6.5px;font-weight:700;letter-spacing:1px;text-transform:uppercase;color:#555;height:22px;line-height:22px}
.client-grid{display:grid;grid-template-columns:repeat(3,184px);gap:10px 24px;justify-content:center;height:170px}
.client-tile{height:80px;background:var(--tile)}
.client-tile.placeholder{background:#c9c9c9;display:flex;flex-direction:column;align-items:center;justify-content:center;color:#666;font-size:6.5px}

/* call to action */
.cta{margin-top:8px;height:36px;border:1px solid var(--line);display:flex;align-items:center;justify-content:space-between;padding:0 12px}
.cta p{font-size:8px;font-weight:600}

/* blog */
.blog{display:flex;gap:20px;height:240px;padding-top:4px}
.blog-lead{width:170px}
.blog-lead-photo{height:100px;background:linear-gradient(135deg,#e8e8e8,#c7ccd0)}
.blog-lead h4{font-size:7px;font-weight:700;margin:6px 0 3px}
.blog-lead p{color:var(--muted);font-size:6px}
.posts{flex:1}
.post{border-bottom:1px solid var(--line);padding:6px 0 7px}
.post:last-child{border:0}
.post h4{font-size:7px;font-weight:700;margin-bottom:3px}
.post p{color:var(--muted);font-size:6px}

/* light footer */
.footer-top{background:var(--soft);height:140px;border-top:1px solid var(--line)}
.footer-top .wrap{display:flex;justify-content:space-between;padding-top:12px}
.footer-top h5{font-size:7px;font-weight:700;margin-bottom:6px}
.col-twitter{width:200px}
.col-twitter p{color:var(--muted);font-size:6px;margin-bottom:6px}
.col-testimonials{width:230px}
.testimonial{display:flex;gap:8px;margin-bottom:10px}
.avatar{width:26px;height:26px;border-radius:50%;background:#3a3a3a;flex:none}
.testimonial p{color:var(--muted);font-size:6px}
.col-contact{width:180px}
.field{height:13px;background:var(--white);border:1px solid var(--line);margin-bottom:4px;font-size:5.5px;color:#999;padding:1px 4px}
.field.tall{height:28px}
.col-contact .btn{float:right}

/* dark footer */
.footer-main{background:var(--footer);height:84px;color:var(--footer-text)}
.footer-main .wrap{display:flex;justify-content:space-between;padding-top:8px}
.footer-main h6{font-size:6.5px;color:var(--white);font-weight:700;margin-bottom:4px}
.footer-main li{list-style:none;font-size:5.5px;line-height:1.7;display:flex;align-items:center;gap:4px}
.footer-col{width:140px}
.mark{width:6px;height:6px;border-radius:50%;background:#555;flex:none}
.newsletter{display:flex;margin-top:3px}
.newsletter span{height:10px;width:80px;background:#3a3a3a}
.newsletter b{height:10px;width:18px;background:var(--green)}
.photo-stream{display:grid;grid-template-columns:repeat(4,17px);gap:3px}
.photo-stream i{height:17px;background:#555}
.photo-stream i:nth-child(3n){background:#6e6e6e}
.footer-bar{background:var(--footer-deep);height:16px;color:#888;font-size:5.5px}
.footer-bar .wrap{display:flex;justify-content:flex-end;gap:10px;line-height:16px}
</style>
</head>
<body>

<header class="site-header">
  <div class="wrap">
    <div class="brand"><span class="brand-dot"></span>Wyllard Benick Consulting</div>
    <nav class="main-nav">
      <a class="active">Home</a><a>About</a><a>Services</a><a>Industries</a><a>Blog</a><a>Contact</a>
    </nav>
  </div>
</header>

<section class="hero">
  <div class="wrap">
    <div class="hero-photo" role="img" aria-label="Photo of a smiling business team joining hands"></div>
    <div class="hero-copy">
      <h1>Be successful,<br>it's easy!</h1>
      <h2>we work for your profit!</h2>
      <p>We support finance and supply chain teams with clear processes and reliable systems, from first review to full implementation and beyond.</p>
      <a class="btn">Find out more today</a>
    </div>
  </div>
  <div class="slide-arrow prev"><svg width="6" height="10"><path d="M5 1L1 5l4 4" stroke="#fff" fill="none" stroke-width="1.5"/></svg></div>
  <div class="slide-arrow next"><svg width="6" height="10"><path d="M1 1l4 4-4 4" stroke="#fff" fill="none" stroke-width="1.5"/></svg></div>
</section>
<div class="dots"><i class="on"></i><i></i><i></i></div>

<section class="features">
  <div class="wrap">
    <div class="feature">
      <svg width="18" height="18" viewBox="0 0 18 18"><circle cx="9" cy="9" r="7" fill="none" stroke="#333" stroke-width="1.5"/><path d="M9 5v4l3 2" stroke="#333" stroke-width="1.5" fill="none"/></svg>
      <h3>Finance process review</h3>
      <p>We examine how your finance team works today and map a practical path to faster closes, sharper reporting and tighter controls.</p>
      <a class="more">Read more</a>
    </div>
    <div class="feature">
      <svg width="18" height="18" viewBox="0 0 18 18"><circle cx="9" cy="9" r="7" fill="none" stroke="#333" stroke-width="1.5"/><circle cx="9" cy="9" r="3" fill="#333"/></svg>
      <h3>Supply chain systems</h3>
      <p>From planning to delivery, we design and implement systems that keep stock, orders and suppliers working together smoothly.</p>
      <a class="more">Read more</a>
    </div>
    <div class="feature">
      <svg width="18" height="18" viewBox="0 0 18 18"><circle cx="9" cy="10" r="6.5" fill="none" stroke="#333" stroke-width="1.5"/><path d="M9 10V6M7 2h4" stroke="#333" stroke-width="1.5"/></svg>
      <h3>Implementation support</h3>
      <p>Our consultants stay with you through rollout, training and review so that every change delivers lasting value to the business.</p>
      <a class="more">Read more</a>
    </div>
  </div>
</section>

<section class="clients wrap">
  <div class="section-title">Our Clients</div>
  <div class="client-grid">
    <div class="client-tile placeholder"><strong>Your Business Image</strong>184 x 80</div>
    <div class="client-tile" role="img" aria-label="Client work showcase"></div>
    <div class="client-tile" role="img" aria-label="Client work showcase"></div>
    <div class="client-tile" role="img" aria-label="Client work showcase"></div>
    <div class="client-tile" role="img" aria-label="Client work showcase"></div>
    <div class="client-tile" role="img" aria-label="Client work showcase"></div>
  </div>
</section>
<div class="dots"><i class="on"></i><i></i></div>

<section class="wrap">
  <div class="cta">
    <p>Ready to improve your finance and supply chain results? <span class="green">Talk to us today.</span></p>
    <a class="btn">Get a free consultation</a>
  </div>

  <div class="section-title" style="margin-top:8px">Latest from the Blog</div>
  <div class="blog">
    <article class="blog-lead">
      <div class="blog-lead-photo" role="img" aria-label="Photo of a consultant at work"></div>
      <h4>Smarter Optimal Financial Program</h4>
      <p>A short look at how a structured finance program helps growing companies plan with confidence and act on reliable numbers.</p>
      <a class="more">Read more</a>
    </article>
    <div class="posts">
      <article class="post">
        <h4>Five signs your month-end close needs attention</h4>
        <p>Late adjustments, manual spreadsheets and unclear ownership slow every close. We share simple steps that shorten the cycle and build trust in the figures your leaders rely on.</p>
        <a class="more">Read more</a>
      </article>
      <article class="post">
        <h4>Building a supply chain that can absorb change</h4>
        <p>Demand shifts quickly. Clear data, flexible planning and the right system settings let your team respond without losing control of cost or service levels.</p>
        <a class="more">Read more</a>
      </article>
      <article class="post">
        <h4>Choosing the right partner for a system rollout</h4>
        <p>A successful implementation depends on people as much as software. Here is what to ask before you sign with any implementation partner.</p>
        <a class="more">Read more</a>
      </article>
    </div>
  </div>
</section>

<footer>
  <div class="footer-top">
    <div class="wrap">
      <div class="col-twitter">
        <h5>Latest from Updates</h5>
        <p>New article on faster month-end closing is now live on our blog. <span class="green">2 hours ago</span></p>
        <p>Join our free webinar on supply chain planning next week. <span class="green">1 day ago</span></p>
      </div>
      <div class="col-testimonials">
        <h5>Client Testimonials</h5>
        <div class="testimonial"><div class="avatar" role="img" aria-label="Client portrait"></div><p>The team helped us cut our close from ten days to four. Clear, practical and always available.</p></div>
        <div class="testimonial"><div class="avatar" role="img" aria-label="Client portrait"></div><p>Our new planning system went live on time and our stock levels have never been healthier.</p></div>
      </div>
      <div class="col-contact">
        <h5>Let's get in touch</h5>
        <div class="field">Your Name</div>
        <div class="field">Your Email</div>
        <div class="field tall">Your Message</div>
        <a class="btn">Send</a>
      </div>
    </div>
  </div>

  <div class="footer-main">
    <div class="wrap">
      <div class="footer-col">
        <h6>Get in Touch</h6>
        <ul><li>Wyllard Benick Consulting</li><li>14 Harbour Lane, Suite 3</li><li>Phone: 555 0142 880</li></ul>
        <h6 style="margin-top:3px">Sign up for our Newsletter</h6>
        <div class="newsletter"><span></span><b></b></div>
      </div>
      <div class="footer-col">
        <h6>Social Media</h6>
        <ul><li><span class="mark"></span>Follow our updates</li><li><span class="mark"></span>Join our network</li><li><span class="mark"></span>Watch our videos</li><li><span class="mark"></span>Read our news feed</li></ul>
      </div>
      <div class="footer-col">
        <h6>Our Services</h6>
        <ul><li>Finance process review</li><li>Supply chain systems</li><li>Implementation support</li><li>Training and review</li></ul>
      </div>
      <div class="footer-col" style="width:80px">
        <h6>Photo Stream</h6>
        <div class="photo-stream" role="img" aria-label="Grid of recent event photos"><i></i><i></i><i></i><i></i><i></i><i></i><i></i><i></i></div>
      </div>
    </div>
  </div>
  <div class="footer-bar"><div class="wrap"><a>Home</a><a>About</a><a>Services</a><a>Contact</a></div></div>
</footer>

</body>
</html>
```